mosswickpartners Business Card Design

Business card with logo design for mosswickpartners. We are a group of professional project managers based on the Pareto Principle that 80% of the work is done by 20% of the people. I have a makeshift logo that uses a pi chart with 30% and 20% and the 20% pie slice is set slightly out and up. Have played around with a teal and orange colour scheme.

Industry/Entity Type

Business

Contact Information for Business Card

Harold Penbury
Director
mosswickpartners

0487 263019

```html
<!DOCTYPE html>
<html lang="en">
<head>
<meta charset="utf-8">
<title>mosswickpartners Business Card</title>
<link rel="stylesheet" href="https://fonts.googleapis.com/css2?family=Mulish:wght@500;600;700&display=swap">
<style>
  :root {
    --backdrop: #e9e4dc;
    --card-white: #ffffff;
    --navy: #0b1f3d;
    --logo-grey: #4d5358;
    --accent-orange: #f2472a;
    --text-light: #ffffff;
  }
  * { margin: 0; padding: 0; box-sizing: border-box; }
  html, body {
    width: 1200px;
    height: 960px;
    overflow: hidden;
    background: var(--backdrop);
    font-family: "Mulish", sans-serif;
  }
  .business-card {
    position: absolute;
    left: 250px;
    top: 280px;
    width: 700px;
    height: 400px;
    background: var(--card-white);
    box-shadow: 0 6px 18px rgba(0, 0, 0, 0.25);
    overflow: hidden;
  }
  .card-shapes {
    position: absolute;
    inset: 0;
    width: 700px;
    height: 400px;
  }
  .brand {
    position: absolute;
    right: 60px;
    top: 96px;
    display: flex;
    align-items: center;
    gap: 12px;
  }
  .brand-dot {
    width: 22px;
    height: 22px;
    border-radius: 50%;
    background: var(--accent-orange);
  }
  .brand-name {
    font-size: 26px;
    font-weight: 600;
    color: var(--logo-grey);
    letter-spacing: 0.3px;
  }
  .contact {
    position: absolute;
    left: 0;
    right: 0;
    top: 238px;
    text-align: center;
    color: var(--text-light);
  }
  .contact-name {
    font-size: 27px;
    font-weight: 700;
    letter-spacing: 0.3px;
    line-height: 1.2;
  }
  .contact-title {
    font-size: 21px;
    font-weight: 500;
    margin-top: 2px;
  }
  .contact-phone {
    font-size: 28px;
    font-weight: 500;
    margin-top: 14px;
    letter-spacing: 0.5px;
  }
  .web-address {
    position: absolute;
    left: 0;
    right: 0;
    bottom: 12px;
    text-align: center;
    font-size: 20px;
    font-weight: 500;
    color: var(--text-light);
    letter-spacing: 0.4px;
  }
</style>
</head>
<body>
  <div class="business-card">
    <svg class="card-shapes" viewBox="0 0 700 400" aria-hidden="true">
      <path class="navy-band" d="M0,228 C200,196 480,190 700,212 L700,400 L0,400 Z" fill="var(--navy)"/>
      <path class="swoosh" d="M100,204 C250,188 430,186 540,196 C420,194 260,196 100,206 Z" fill="var(--navy)"/>
      <rect class="divider" x="0" y="350" width="700" height="4" fill="var(--card-white)"/>
    </svg>

    <div class="brand">
      <span class="brand-dot"></span>
      <span class="brand-name">mosswickpartners</span>
    </div>

    <div class="contact">
      <p class="contact-name">Harold Penbury</p>
      <p class="contact-title">Director</p>
      <p class="contact-phone">0487 263019</p>
    </div>

    <p class="web-address">www.mosswickpartners.com.au</p>
  </div>
</body>
</html>
```